Corrow Family Farm fresh honey jar label

I need a label for jars of honey harvested at our farm. These are for gifts and personal use. We are looking to incorporate our farm brand into the label. We would like the design to take the existing brand and add some element like bees, honey, flowers, or hives to indicate the contents. We want the design to feel homemade and authentic without feeling cheap or hoaky

Requirements
Must have
• The label must be made to fit a 1" x2" rectangular label. The label must include the attached family brand. The label must include the text "Corrow Family Farms" "Pinebrook, USA" "Farm Fresh Honey". The label will be printed on off-white paper
Nice to have
• It would be nice to have illustrations of bees or flowers around the logo or hives or honeycombs. The label should have a vintage feel
Should not have
• The label should not feel overly cartoonish or hoaky

```html
<!DOCTYPE html>
<html lang="en">
<head>
<meta charset="utf-8">
<title>Corrow Family Farms – Farm Fresh Honey Label</title>
<link rel="stylesheet" href="https://fonts.googleapis.com/css2?family=Cinzel:wght@400;500&family=Libre+Baskerville:wght@400;700&display=swap">
<style>
  :root {
    --backdrop: #aaaaaa;
    --label-cream: #ede7dc;
    --rust: #b8632a;
    --brown: #4a3823;
    --honey: #e6a868;
    --sage: #b9c1a9;
    --ribbon-text: #f6efe4;
  }
  html, body {
    margin: 0;
    padding: 0;
    overflow: hidden;
  }
  .canvas {
    width: 1200px;
    height: 919px;
    background: var(--backdrop);
    display: flex;
    align-items: center;
    justify-content: center;
  }
  .honey-label {
    width: 410px;
    height: 859px;
    display: block;
    filter: drop-shadow(2px 4px 5px rgba(0,0,0,0.25));
  }
  .label-edge { fill: var(--rust); }
  .label-paper { fill: var(--label-cream); }
  .label-rule { fill: none; stroke: var(--brown); stroke-width: 2; }
  .brand-square { fill: var(--brown); }
  .brand-name {
    font-family: "Cinzel", serif;
    font-weight: 500;
    fill: var(--brown);
    font-size: 34px;
    letter-spacing: 5px;
  }
  .ribbon { fill: var(--rust); }
  .ribbon-text {
    font-family: "Libre Baskerville", serif;
    font-weight: 700;
    font-size: 22px;
    letter-spacing: 6px;
    fill: var(--ribbon-text);
  }
  .farm-name {
    font-family: "Cinzel", serif;
    font-weight: 400;
    fill: var(--rust);
    font-size: 80px;
    letter-spacing: 4px;
  }
  .farm-sub {
    font-family: "Cinzel", serif;
    font-weight: 400;
    fill: var(--brown);
    font-size: 45px;
    letter-spacing: 3px;
  }
  .place, .weight {
    font-family: "Libre Baskerville", serif;
    fill: var(--brown);
  }
  .place { font-size: 19px; letter-spacing: 4px; }
  .weight { font-size: 18px; letter-spacing: 2px; }
</style>
</head>
<body>
<main class="canvas">
  <svg class="honey-label" viewBox="0 0 530 1110" xmlns="http://www.w3.org/2000/svg">
    <defs>
      <radialGradient id="artwork-wash" cx="50%" cy="50%" r="60%">
        <stop offset="0%" stop-color="var(--honey)" stop-opacity="0.55"/>
        <stop offset="55%" stop-color="var(--sage)" stop-opacity="0.35"/>
        <stop offset="100%" stop-color="var(--label-cream)" stop-opacity="0"/>
      </radialGradient>
    </defs>

    <path class="label-edge" d="M0,122 L40,116 C130,108 150,0 265,0 C380,0 400,108 490,116 L530,122 L530,1105 Q265,1075 0,1105 Z"/>
    <path class="label-paper" d="M9,129 L42,124 C138,115 158,9 265,9 C372,9 392,115 488,124 L521,129 L521,1090 Q265,1062 9,1090 Z"/>
    <path class="label-rule" d="M18,137 L44,132 C146,122 166,19 265,19 C364,19 384,122 486,132 L512,137 L512,1077 Q265,1050 18,1077 Z"/>

    <g class="brand-mark">
      <rect class="brand-square" x="233" y="110" width="64" height="64"/>
      <text class="brand-name" x="265" y="236" text-anchor="middle">CORROW FARM</text>
    </g>

    <path class="ribbon" d="M55,382 L90,340 Q265,270 440,340 L475,382 L470,438 Q265,350 60,438 Z"/>
    <path id="ribbon-curve" d="M70,413 Q265,318 460,413" fill="none"/>
    <text class="ribbon-text"><textPath href="#ribbon-curve" startOffset="50%" text-anchor="middle">FARM FRESH HONEY</textPath></text>

    <rect class="label-artwork" x="20" y="420" width="490" height="345" fill="url(#artwork-wash)" role="img" aria-label="Illustration of a honey bee over a honeycomb outline, flanked by sprigs of orange and pink wildflowers with green leaves"/>

    <text class="farm-name" x="265" y="862" text-anchor="middle">CORROW</text>
    <text class="farm-sub" x="265" y="914" text-anchor="middle">FAMILY FARMS</text>
    <text class="place" x="265" y="957" text-anchor="middle">PINEBROOK, USA</text>
    <text class="weight" x="265" y="1030" text-anchor="middle">100g</text>
  </svg>
</main>
</body>
</html>
```